Selka Marven Photography Business Card

I need a new business card/ possibly design to use for other marking materials ... I have included my logo below in a few different colors, but can also provide the logo in additional colors and sizes. I would love a card the expresses clean, simple and classy.

Target Market(s)

Portrait photography clients, child photography clients

Industry/Entity Type

Photographer

Contact Information for Business Card

Selka Marven Photography, Fernhollow MA, www.selkamarvenphotography-demo.com
T. 555-203-1946 E. selkamarvenphoto@mailbox-demo.com

Colors
33b8a4
eea4c8
5c5c5c

Requirements
Must have
• I would like to include my logo on card.
Nice to have
• I also like the color brown as well as the choices below. I would like a simple, elegant card, something classy.

```html
<!DOCTYPE html>
<html lang="en">
<head>
<meta charset="utf-8">
<title>Selka Marven Photography – Business Card</title>
<link rel="stylesheet" href="https://fonts.googleapis.com/css2?family=Lato:wght@300;400;700&display=swap">
<style>
  :root {
    --backdrop: #e3e8e8;
    --card: #ffffff;
    --ink: #1f1f1f;
    --ink-soft: #3a3a3a;
    --teal: #2aa68f;
    --photo-warm: #c98a3a;
    --photo-deep: #5a3a22;
    --photo-gold: #e0a94a;
    --light-text: #f4f1ea;
  }
  * { box-sizing: border-box; margin: 0; padding: 0; }
  html, body {
    width: 1200px; height: 900px; overflow: hidden;
    background: var(--backdrop);
    font-family: "Lato", Arial, sans-serif;
  }
  .canvas {
    width: 1200px; height: 900px;
    display: flex; align-items: center; justify-content: center; gap: 48px;
  }
  .card {
    width: 525px; height: 300px;
    position: relative; overflow: hidden;
    box-shadow: 0 8px 22px rgba(0,0,0,0.14);
  }
  /* Front side */
  .card--front .photo {
    position: absolute; inset: 0;
    background:
      radial-gradient(ellipse at 30% 40%, var(--photo-gold) 0%, transparent 55%),
      radial-gradient(ellipse at 75% 30%, #8a6a40 0%, transparent 60%),
      linear-gradient(160deg, var(--photo-warm) 0%, #9b6a35 45%, var(--photo-deep) 100%);
  }
  .card--front .brand-overlay {
    position: absolute; left: 120px; top: 128px;
    color: var(--light-text);
    font-weight: 300; font-size: 26px; letter-spacing: 2px;
    text-transform: lowercase;
  }
  /* Back side */
  .card--back { background: var(--card); color: var(--ink); }
  .brand {
    position: absolute; left: 130px; top: 70px;
    display: flex; align-items: center; gap: 12px;
    font-weight: 300; font-size: 28px; letter-spacing: 1px;
    color: var(--ink);
  }
  .brand__mark { width: 12px; height: 12px; border-radius: 50%; background: var(--ink); }
  .role {
    position: absolute; right: 34px; top: 142px;
    font-size: 10px; letter-spacing: 0.3px; text-transform: uppercase;
  }
  .person {
    position: absolute; left: 40px; top: 176px;
    font-size: 24px; letter-spacing: 0.5px; text-transform: uppercase;
    font-weight: 300;
  }
  .person strong { font-weight: 400; }
  .rule {
    position: absolute; left: 40px; right: 30px; top: 160px;
    height: 3px; background: var(--teal);
  }
  .rule--lower { left: 40px; right: 200px; top: 210px; }
  .contact {
    position: absolute; left: 40px; top: 222px;
    font-size: 10.5px; line-height: 15px; color: var(--ink-soft);
    list-style: none;
  }
  .contact .label { color: var(--teal); }
  .contact .email { margin-left: 8px; }
</style>
</head>
<body>
  <main class="canvas">
    <section class="card card--front">
      <div class="photo" role="img" aria-label="Family portrait photograph: a mother walking hand in hand with two young boys along an autumn forest path"></div>
      <div class="brand-overlay">Selka Marven Photography</div>
    </section>

    <section class="card card--back">
      <div class="brand"><span class="brand__mark"></span>Selka Marven Photography</div>
      <div class="role">Managing Director</div>
      <div class="rule"></div>
      <h1 class="person"><strong>Selka</strong> Marven</h1>
      <div class="rule rule--lower"></div>
      <ul class="contact">
        <li><span class="label">Address:</span> Fernhollow MA</li>
        <li><span class="label">Phone:</span> 555-203-1946<span class="email"><span class="label">Email:</span> selkamarvenphoto@mailbox-demo.com</span></li>
        <li><span class="label">Website:</span> www.selkamarvenphotography-demo.com</li>
      </ul>
    </section>
  </main>
</body>
</html>
```